Business card for a vending machine business

I need a business card for my vending machine business. The name is Brightwell Snacks, LLC. The card is one-sided, and landscape format. Not portrait.

The information for the card is as follows:

Dora Quinlan
Owner
(555) 314-2096
Brightwellsnacks.example
Info@brightwellsnacks.example

I'd like colors and design elements to match what's in my logo and company name. I'd like to have the checkered flag or racing stripe if possible You can use a border if youd like. You can use a background color if it looks nice and doesn't clash with the logo
Use your creativity. But a white background is perfectly fine. The card can be as simple, yet gets the point across to match the company name and logo.

I uploaded a copy of my logo. I also uploaded a businesses card I started to create, but since it was missing something, I gave up. Another upload has a red thunderbolt and the checkerer flag. Those two uploads are for inspiration. Again, please make sure to make the card landscape, not portrait. Thank you, designers. Good luck to all.

```html
<!DOCTYPE html>
<html lang="en">
<head>
<meta charset="utf-8">
<title>Brightwell Snacks – Business Card</title>
<link rel="stylesheet" href="https://fonts.googleapis.com/css2?family=Montserrat:wght@400;600;800&display=swap">
<style>
  :root {
    --brand-red: #e8121b;
    --brand-red-soft: #f4525a;
    --ink: #1d1d1d;
    --card-white: #ffffff;
    --backdrop: #e9e9eb;
  }
  * { box-sizing: border-box; margin: 0; padding: 0; }
  html, body {
    width: 1200px; height: 1200px; overflow: hidden;
    background: var(--backdrop);
    font-family: "Montserrat", sans-serif;
  }
  .sheet {
    width: 1200px; height: 1200px;
    display: flex; flex-direction: column; align-items: center; justify-content: center;
    gap: 60px;
  }
  .card {
    position: relative;
    width: 900px; height: 514px;
    background: var(--card-white);
    border-radius: 30px;
    overflow: hidden;
    border-bottom: 3px solid var(--brand-red);
    box-shadow: 0 10px 30px rgba(0,0,0,0.12);
  }
  .race-band {
    position: absolute; inset: 0;
    width: 100%; height: 100%;
  }
  .wordmark {
    position: absolute;
    display: flex; align-items: center; gap: 14px;
    color: var(--brand-red);
    font-weight: 800;
    text-transform: uppercase;
    letter-spacing: 1px;
    line-height: 1;
    white-space: nowrap;
  }
  .wordmark .mark-square {
    width: 34px; height: 34px;
    background: var(--brand-red);
    flex: none;
  }
  .front .wordmark { top: 110px; right: 60px; font-size: 40px; }
  .back .wordmark { top: 150px; left: 50%; transform: translateX(-50%); font-size: 54px; }
  .back .wordmark .mark-square { width: 46px; height: 46px; }

  .contact-block {
    position: absolute;
    left: 0; top: 196px;
    padding-left: 58px;
  }
  .accent-bar {
    position: absolute;
    left: 0; top: 8px;
    width: 14px; height: 76px;
    background: var(--brand-red);
  }
  .person-name {
    color: var(--brand-red);
    font-weight: 600;
    font-size: 42px;
    letter-spacing: 1px;
    line-height: 1.05;
  }
  .person-role {
    color: var(--ink);
    font-weight: 400;
    font-size: 34px;
    letter-spacing: 1px;
    margin-bottom: 16px;
  }
  .contact-list { list-style: none; }
  .contact-list li {
    display: flex; align-items: center; gap: 18px;
    color: var(--ink);
    font-size: 28px;
    line-height: 1.4;
  }
  .contact-list svg { width: 30px; height: 30px; flex: none; }
</style>
</head>
<body>
<main class="sheet">

  <section class="card front">
    <svg class="race-band" viewBox="0 0 900 514" preserveAspectRatio="none" role="img" aria-label="Red checkered racing stripe running diagonally along the lower right of the card">
      <defs>
        <linearGradient id="bandFront" x1="0" y1="1" x2="1" y2="0">
          <stop offset="0" stop-color="var(--brand-red)"/>
          <stop offset="1" stop-color="var(--brand-red-soft)"/>
        </linearGradient>
      </defs>
      <polygon points="340,514 900,300 900,345 458,514" fill="url(#bandFront)"/>
    </svg>

    <div class="wordmark"><span class="mark-square"></span>Brightwell Snacks</div>

    <div class="contact-block">
      <span class="accent-bar"></span>
      <h1 class="person-name">DORA QUINLAN</h1>
      <p class="person-role">OWNER</p>
      <ul class="contact-list">
        <li>
          <svg viewBox="0 0 24 24" aria-hidden="true"><path fill="var(--brand-red)" d="M6.6 10.8a15.1 15.1 0 0 0 6.6 6.6l2.2-2.2a1 1 0 0 1 1-.25 11.4 11.4 0 0 0 3.6.57 1 1 0 0 1 1 1V20a1 1 0 0 1-1 1A17 17 0 0 1 3 4a1 1 0 0 1 1-1h3.5a1 1 0 0 1 1 1c0 1.25.2 2.45.57 3.57a1 1 0 0 1-.25 1z"/></svg>
          (555) 314-2096
        </li>
        <li>
          <svg viewBox="0 0 24 24" aria-hidden="true" fill="none" stroke="var(--brand-red)" stroke-width="1.8"><circle cx="12" cy="12" r="9.5"/><ellipse cx="12" cy="12" rx="4" ry="9.5"/><path d="M2.5 12h19M4 7h16M4 17h16"/></svg>
          Brightwellsnacks.example
        </li>
        <li>
          <svg viewBox="0 0 24 24" aria-hidden="true"><rect x="2" y="5" width="20" height="14" fill="var(--brand-red)"/><path d="M2 5l10 8 10-8" fill="none" stroke="#fff" stroke-width="1.6"/></svg>
          Info@brightwellsnacks.example
        </li>
      </ul>
    </div>
  </section>

  <section class="card back">
    <svg class="race-band" viewBox="0 0 900 514" preserveAspectRatio="none" role="img" aria-label="Red checkered racing stripe running diagonally along the lower right of the card">
      <defs>
        <linearGradient id="bandBack" x1="0" y1="1" x2="1" y2="0">
          <stop offset="0" stop-color="var(--brand-red)"/>
          <stop offset="1" stop-color="var(--brand-red-soft)"/>
        </linearGradient>
      </defs>
      <polygon points="300,514 900,230 900,280 406,514" fill="url(#bandBack)"/>
    </svg>

    <div class="wordmark"><span class="mark-square"></span>Brightwell Snacks</div>
  </section>

</main>
</body>
</html>
```